Brightfernrx website

We are a weight loss clinic and we need a website built. please look at these websites for content and style. Just need like 5 pages see samples. AI files of logo are not avail yet so use sample for place set

https://glowshiftstudio.com/
ortanvital.com
https://pinecrestclinicalbodybalance.com/
https://yourslimmingnook.com/
https://qrvskinstudio.com/treatments/weight-loss-injections/

Target Market(s)

Women

Industry/Entity Type

weight loss

Coding

Coded - Design and coding required

Number of Pages Required

5+ page

Requirements
Nice to have
• please make look like a medspa website

```html
<!DOCTYPE html>
<html lang="en">
<head>
<meta charset="utf-8">
<title>Brightfernrx — Weight Loss Clinic</title>
<link href="https://fonts.googleapis.com/css2?family=Lora:wght@400;500&family=Open+Sans:wght@400;600;700&display=swap" rel="stylesheet">
<style>
:root{
  --blue:#1f8ac9;
  --blue-deep:#2a7eb2;
  --green:#7fb241;
  --ink:#2f3b45;
  --body:#6b7680;
  --dark:#363c45;
  --line:#e3e7ea;
  --white:#ffffff;
}
*{box-sizing:border-box;margin:0;padding:0}
html,body{width:1200px;height:4504px;overflow:hidden}
body{font-family:"Open Sans",Arial,sans-serif;color:var(--body);background:var(--white);font-size:14px;line-height:1.6}
h1,h2,h3{font-family:"Lora",Georgia,serif;font-weight:400;color:var(--ink)}
.section{position:relative;width:1200px;overflow:hidden}
.btn{display:inline-block;background:var(--green);color:var(--white);font-size:13px;font-weight:600;padding:9px 22px;border-radius:2px;text-decoration:none}
.photo{position:absolute}

/* header */
.site-header{height:112px;display:flex;align-items:center;padding:0 60px;background:var(--white);position:relative;z-index:2}
.brand{display:flex;align-items:center;gap:10px;font-weight:700;font-size:26px;color:var(--blue);letter-spacing:.5px}
.brand-dot{width:26px;height:26px;border-radius:50%;background:var(--green)}
.main-nav{display:flex;gap:30px;margin-left:150px;font-size:12px;font-weight:600;color:var(--ink)}
.main-nav .active{color:var(--blue);border-bottom:2px solid var(--blue);padding-bottom:4px}
.header-actions{margin-left:auto;display:flex;align-items:center;gap:18px}
.book-btn{background:var(--blue);color:#fff;font-size:12px;font-weight:600;padding:8px 18px;border-radius:2px}
.call{display:flex;align-items:center;gap:8px;font-size:11px;color:var(--body)}
.call strong{display:block;font-size:16px;color:var(--ink)}
.call-icon{width:26px;height:26px;border-radius:50%;background:var(--green);display:flex;align-items:center;justify-content:center}

/* hero */
.hero{height:628px;background:linear-gradient(180deg,#bfe4ee 0%,#9fd3e0 45%,#e8ddc9 100%)}
.hero .photo{right:0;top:0;width:560px;height:628px;background:linear-gradient(160deg,#c8a78a,#a87c60 60%,#dcc7b0)}
.hero-copy{position:absolute;left:160px;top:100px;width:400px}
.hero-copy h1{font-size:58px;line-height:1.15;color:#fff;margin-bottom:22px}
.hero-copy p{color:#fff;font-size:14px;margin-bottom:24px}
.dots{position:absolute;left:545px;top:522px;display:flex;gap:10px}
.dots span{width:10px;height:10px;background:#2d3a44;display:block}
.dots span.on{background:#fff}

/* about */
.about{height:480px;background:#fff}
.about .photo{left:0;top:0;width:680px;height:480px;background:linear-gradient(120deg,#dfe9ef,#9fb8c8 55%,#5a88b0)}
.about-copy{position:absolute;left:752px;top:60px;width:320px}
.about-copy h2,.change-copy h2{font-size:30px;margin-bottom:10px}
.rule{width:40px;height:3px;background:var(--blue);margin-bottom:22px}
.about-copy p{margin-bottom:26px}
.about .leaf{position:absolute;right:20px;bottom:40px;width:140px;height:150px;border-radius:50%;background:#eef4e8}

/* change */
.change{height:580px;background:linear-gradient(90deg,#f6eeec,#efe4e1)}
.change .photo{left:660px;top:0;width:540px;height:580px;background:linear-gradient(180deg,#efe4df,#d6b39d 60%,#e9dbd4)}
.change-copy{position:absolute;left:212px;top:80px;width:390px}
.change-copy p{margin-bottom:30px}

/* services */
.services{height:860px;background:linear-gradient(180deg,#fff 0%,#fbfaf1 40%,#eef3e6 70%,#fff 100%)}
.services h2{text-align:center;font-size:32px;padding-top:60px}
.services .rule{margin:10px auto 0}
.service{position:absolute;width:230px;text-align:center}
.service h3{font-family:"Open Sans",sans-serif;font-size:13px;font-weight:700;color:var(--ink);margin:12px 0 8px}
.service p{font-size:11px;line-height:1.5}
.divider{position:absolute;width:1px;background:var(--line)}
.services .photo{left:240px;top:420px;width:720px;height:440px;background:linear-gradient(100deg,#f0efe7,#cdb6a5 50%,#f3f1ea)}

/* stories */
.stories{height:480px;background:linear-gradient(180deg,#3d434c,#2f343b)}
.stories h2{color:#fff;text-align:center;font-size:32px;padding-top:56px}
.stories .rule{margin:10px auto 0;background:#fff}
.stories .photo{left:80px;top:140px;width:420px;height:340px;background:linear-gradient(180deg,#7b6557,#4a3d36)}
.quote{position:absolute;left:580px;top:150px;width:520px;color:#dfe3e6;font-size:14px}
.quote .mark{font-family:"Lora",serif;font-size:60px;color:#fff;line-height:1;position:absolute;left:-50px;top:-6px}
.quote cite{display:block;margin-top:24px;font-style:normal;color:#aeb5bb;font-size:12px}
.arrows{position:absolute;left:1010px;top:385px;display:flex;gap:10px}

/* features */
.features{height:480px;background:#fff}
.feature{position:absolute;top:70px;width:380px;text-align:center}
.feature h3{font-family:"Open Sans",sans-serif;font-weight:700;font-size:16px;margin:16px 0 14px}
.feature p{font-size:12px;margin-bottom:24px}
.icon-circle{width:92px;height:92px;border-radius:50%;background:var(--blue);margin:0 auto;display:flex;align-items:center;justify-content:center}
.features .leaf-a{position:absolute;left:0;bottom:0;width:200px;height:180px;background:#e5efdb;border-radius:0 100% 0 0}
.features .leaf-b{position:absolute;right:0;top:0;width:220px;height:190px;background:#e8f0e0;border-radius:0 0 0 100%}
.features .split{position:absolute;left:600px;top:70px;width:1px;height:360px;background:var(--line)}

/* cta */
.cta{height:540px;background:linear-gradient(180deg,#fff,#eef1f2)}
.cta .photo{left:600px;top:0;width:600px;height:540px;background:linear-gradient(160deg,#dbe6ec,#a9b9c4 50%,#d8cfc2)}
.cta-copy{position:absolute;left:80px;top:90px;width:420px}
.cta-copy h2{font-size:32px;line-height:1.3;margin-bottom:20px}
.cta-copy p{margin-bottom:26px}

/* footer */
.site-footer{height:344px;background:var(--blue-deep);color:#d7e8f3;font-size:12px}
.site-footer .brand{position:absolute;left:120px;top:70px;color:#fff}
.site-footer .brand-dot{background:#fff}
.fcol{position:absolute;top:50px}
.fcol h4{color:#fff;font-size:13px;font-weight:700;margin-bottom:14px}
.frow{display:flex;align-items:flex-start;gap:10px;margin-bottom:10px}
.ficon{width:24px;height:24px;border-radius:50%;background:#fff;flex:none}
.fcol ul{list-style:none}
.fcol li{margin-bottom:4px;display:flex;gap:8px;align-items:center}
.fcol li::before{content:"";width:4px;height:4px;background:#fff;border-radius:50%}
.copyright{position:absolute;left:0;right:0;bottom:28px;text-align:center;font-size:11px;color:#cfe2ef}
.site-footer .sep{position:absolute;left:80px;right:80px;bottom:64px;height:1px;background:rgba(255,255,255,.25)}
</style>
</head>
<body>

<header class="site-header">
  <div class="brand"><span class="brand-dot"></span>BRIGHTFERNRX</div>
  <nav class="main-nav">
    <span class="active">HOME</span><span>ABOUT US</span><span>SERVICES</span><span>SPECIALS</span><span>BLOG</span><span>CONTACT US</span>
  </nav>
  <div class="header-actions">
    <span class="book-btn">Book online</span>
    <div class="call">
      <span class="call-icon"><svg width="14" height="14" viewBox="0 0 24 24"><path fill="#fff" d="M6.6 10.8a15 15 0 006.6 6.6l2.2-2.2c.3-.3.7-.4 1-.2 1.1.4 2.3.6 3.6.6.6 0 1 .4 1 1V20c0 .6-.4 1-1 1C10.6 21 3 13.4 3 4c0-.6.4-1 1-1h3.5c.6 0 1 .4 1 1 0 1.3.2 2.5.6 3.6.1.3 0 .7-.2 1z"/></svg></span>
      <div>Call us<strong>+1 555 014 2290</strong></div>
    </div>
  </div>
</header>

<section class="section hero">
  <div class="photo" role="img" aria-label="Photo of a fit woman in swimwear on a sunny beach"></div>
  <div class="hero-copy">
    <h1>Weight<br>Loss Clinic</h1>
    <p>Our caring team builds a plan around your body, your goals and your life, with steady support from the first visit to lasting, healthy results.</p>
    <a class="btn">Read More</a>
  </div>
  <div class="dots"><span class="on"></span><span></span><span></span><span></span></div>
</section>

<section class="section about">
  <div class="photo" role="img" aria-label="Photo of a man exercising with blue dumbbells"></div>
  <div class="about-copy">
    <h2>About Us</h2>
    <div class="rule"></div>
    <p>We are a medical weight loss clinic with a spa feel. Our doctors and nurses guide each client with care, clear plans and honest advice, so every step toward your goal feels calm, safe and well supported. We listen first, then shape a program that fits your daily routine and helps you keep the results for good.</p>
    <a class="btn">Read More</a>
  </div>
  <div class="leaf" role="img" aria-label="Soft green leaf decoration"></div>
</section>

<section class="section change">
  <div class="change-copy">
    <h2>Change Your Life<br>for the Better!</h2>
    <div class="rule"></div>
    <p>Small changes grow into big results. With a tailored plan, regular check-ins and gentle coaching, you will build habits that last. We help you eat well, move more and feel confident in your own skin, with real progress you can see and measure from week to week.</p>
    <a class="btn">Read More</a>
  </div>
  <div class="photo" role="img" aria-label="Photo of a slim woman in white sportswear measuring her waist"></div>
</section>

<section class="section services">
  <h2>Our Services</h2>
  <div class="rule"></div>

  <div class="service" style="left:90px;top:190px">
    <svg width="44" height="44" viewBox="0 0 44 44"><circle cx="22" cy="22" r="18" fill="none" stroke="#1f8ac9" stroke-width="3"/><path d="M14 22l6 6 10-12" fill="none" stroke="#1f8ac9" stroke-width="3"/></svg>
    <h3>Customized<br>Weightloss Plans</h3>
    <p>A plan shaped around your body, goals and pace, with regular reviews to keep you on track.</p>
  </div>
  <div class="divider" style="left:340px;top:200px;height:180px"></div>
  <div class="service" style="left:365px;top:230px">
    <svg width="44" height="44" viewBox="0 0 44 44"><rect x="8" y="16" width="28" height="12" rx="6" fill="#1f8ac9"/><circle cx="34" cy="10" r="6" fill="#1f8ac9"/></svg>
    <h3>Medications</h3>
    <p>Safe prescription support chosen by our doctors to curb appetite and boost steady progress.</p>
  </div>
  <div class="divider" style="left:610px;top:180px;height:200px"></div>
  <div class="service" style="left:630px;top:200px">
    <svg width="44" height="44" viewBox="0 0 44 44"><rect x="10" y="18" width="24" height="8" rx="2" fill="#1f8ac9" transform="rotate(-45 22 22)"/><path d="M30 8l6 6" stroke="#1f8ac9" stroke-width="3"/></svg>
    <h3>Injections</h3>
    <p>Quick weekly shots that support metabolism and energy, given by trained clinic staff.</p>
  </div>
  <div class="divider" style="left:870px;top:160px;height:200px"></div>
  <div class="service" style="left:890px;top:160px">
    <svg width="44" height="44" viewBox="0 0 44 44"><path d="M22 6c-6 8-8 14-8 20a8 8 0 0016 0c0-6-2-12-8-20z" fill="none" stroke="#1f8ac9" stroke-width="3"/></svg>
    <h3>Laser Lipo</h3>
    <p>Gentle, no-surgery body contouring that targets stubborn areas with little downtime.</p>
  </div>

  <div class="photo" role="img" aria-label="Photo of a woman in sportswear stretching on a mat"></div>
</section>

<section class="section stories">
  <h2>Success Stories</h2>
  <div class="rule"></div>
  <div class="photo" role="img" aria-label="Photo of a fit couple in sportswear, the woman holding a tape measure"></div>
  <blockquote class="quote">
    <span class="mark">&ldquo;</span>
    The team made me feel at ease from day one. My plan was simple to follow, the check-ins kept me honest, and the staff cheered every small win. In six months I lost the weight I had carried for years and I finally feel strong, light and proud of myself again. I tell all my friends about this clinic.
    <cite>Marlow Tenby</cite>
  </blockquote>
  <div class="arrows">
    <svg width="14" height="14" viewBox="0 0 14 14"><path d="M9 2L4 7l5 5" fill="none" stroke="#fff" stroke-width="2"/></svg>
    <svg width="14" height="14" viewBox="0 0 14 14"><path d="M5 2l5 5-5 5" fill="none" stroke="#fff" stroke-width="2"/></svg>
  </div>
</section>

<section class="section features">
  <div class="leaf-a" role="img" aria-label="Soft green leaves decoration"></div>
  <div class="leaf-b" role="img" aria-label="Soft green leaves decoration"></div>
  <div class="feature" style="left:150px">
    <div class="icon-circle"><svg width="40" height="40" viewBox="0 0 44 44"><rect x="10" y="18" width="24" height="8" rx="2" fill="#fff" transform="rotate(-45 22 22)"/><path d="M30 8l6 6" stroke="#fff" stroke-width="3"/></svg></div>
    <h3>Injections</h3>
    <p>Our weekly injection program pairs proven treatments with friendly nurse visits. Each dose is tracked with care so you can feel the change in energy and see steady results over time.</p>
    <a class="btn">Read More</a>
  </div>
  <div class="split"></div>
  <div class="feature" style="left:670px">
    <div class="icon-circle"><svg width="40" height="40" viewBox="0 0 44 44"><rect x="13" y="12" width="18" height="24" rx="3" fill="#fff"/><rect x="15" y="6" width="14" height="5" fill="#fff"/><path d="M22 18v12M16 24h12" stroke="#1f8ac9" stroke-width="3"/></svg></div>
    <h3>Supplements</h3>
    <p>Clinic-grade vitamins and supplements fill gaps in your diet and help your body burn fat well. We pick each one for your needs and review them at every visit.</p>
    <a class="btn">Read More</a>
  </div>
</section>

<section class="section cta">
  <div class="cta-copy">
    <h2>Lorem Ipsum is simply dummy text of the printing and typesetting</h2>
    <p>Ready to start? Book a free talk with our team and we will map out the first steps of your plan together, at a pace that feels right.</p>
    <a class="btn">Contact Us</a>
  </div>
  <div class="photo" role="img" aria-label="Photo of a man jogging on a beach path"></div>
</section>

<footer class="section site-footer">
  <div class="brand"><span class="brand-dot"></span>BRIGHTFERNRX</div>
  <div class="fcol" style="left:430px;width:260px">
    <h4>CONTACT US</h4>
    <div class="frow"><span class="ficon"></span><span>2410 Harbor Crest Avenue, Suite 12,<br>Fernvale, CA 90210</span></div>
    <div class="frow"><span class="ficon"></span><span>+1 555 014 2290</span></div>
    <div class="frow"><span class="ficon"></span><span>hello@brightfernrx.com</span></div>
  </div>
  <div class="fcol" style="left:780px">
    <h4>MENU</h4>
    <ul><li>HOME</li><li>ABOUT US</li><li>SERVICES</li><li>SPECIALS</li><li>BLOG</li><li>CONTACT US</li></ul>
  </div>
  <div class="fcol" style="left:960px">
    <h4>FOLLOW US</h4>
    <div class="frow"><span class="ficon"></span><span>Like us on<br>social</span></div>
    <div class="frow"><span class="ficon"></span><span>Follow us on<br>social</span></div>
    <div class="frow"><span class="ficon"></span><span>Connect on<br>social</span></div>
  </div>
  <div class="sep"></div>
  <p class="copyright">Copyright &copy; 2024 All Rights Reserved</p>
</footer>

</body>
</html>
```